Website for the K7LAVE-Nest research laboratory.

We are a research team working on personality disorders. We would like a website that presents the team members (noting that students change frequently), ongoing projects with active recruitments, the latest publications, student resources, and possibly patient resources.

We have already prepared the logo with Makerflock.

Our research areas:
1- Lifestyle Medicine and BPD
This area focuses on understanding lifestyle habits and their impact on the health of individuals living with Borderline Personality Disorder (BPD). It aims to improve essential components such as sleep, physical activity, and nutrition by identifying and promoting favorable lifestyle habits. The goal is to strengthen emotional regulation and improve overall health by fully integrating the physical dimension into recovery.
2- Interventions Supporting Psychosocial Functioning
Develop the full recovery potential and enhance social and professional integration strategies to support the life journey of patients in all its dimensions. This area focuses on practices and interventions that facilitate a return to an active life and harmonious integration into society.
3- Optimization of Psychotherapeutic Strategies in BPD
Optimize psychotherapeutic approaches for BPD by identifying the most effective methods, adapting them to individual needs, and evaluating their long-term impact. This research area aims to refine and personalize treatments to maximize their therapeutic benefits.
4- Biological Treatments for BPD: Neuromodulation and Pharmacotherapy
Develop and evaluate biological treatments, particularly in neuromodulation and pharmacotherapy, to improve the management of BPD. This area aims to explore scientific advances in these fields to offer complementary and innovative therapeutic options.

Vision
Affiliated with TOBLAVE, our laboratory is dedicated to creating tomorrow's interventions to offer a hopeful future for individuals living with Borderline Personality Disorder. We design and develop innovative solutions that integrate and value each individual, their loved ones, and their community, supporting their personal, social, functional, and physical recovery.

Values

Innovation
Our commitment to innovation guides every step of our research and development. We continually strive to push the boundaries of knowledge and techniques to create new and bold therapeutic solutions tailored to the evolving needs of individuals living with Borderline Personality Disorder.
Hope
We carry the hope of making a real difference in the lives of people living with BPD. This hope drives our work, pushing us to explore therapeutic approaches that offer patients a better and more serene future. By integrating this hope into our research, we are committed to developing interventions that inspire and support the recovery process. Through our research work, we wish to instill and spread hope.
Empathy and Personalization
We believe in a person-centered and inclusive approach where each individual is considered in their uniqueness and with compassion. By actively integrating patients and their experiences into our research, we aim to design solutions that not only meet their specific needs but also value their recovery while respecting their values. We wish to improve the satisfaction of individuals within the care network, promote the integration of their loved ones and their community.

```html
<!DOCTYPE html>
<html lang="en">
<head>
<meta charset="utf-8">
<title>K7LAVE-Nest — Advancing BPD Research and Recovery</title>
<link rel="stylesheet" href="https://fonts.googleapis.com/css2?family=Poppins:wght@400;500;600;700&family=Montserrat:wght@600;700;800;900&family=Anton&display=swap">
<style>
:root{
  --blue:#1b8fd8;
  --blue-dark:#1479c0;
  --green:#3db64a;
  --orange:#f0780f;
  --teal:#14a4a0;
  --cream:#fbf0e4;
  --ink:#121212;
  --text:#3a3a3a;
  --white:#fff;
  --line:#e3e3e3;
}
*{box-sizing:border-box;margin:0;padding:0}
html,body{width:1200px;height:5357px;overflow:hidden}
body{position:relative;font-family:"Poppins",sans-serif;color:var(--text);background:var(--white)}
.abs{position:absolute}
.btn{position:absolute;display:flex;align-items:center;justify-content:center;background:var(--green);color:var(--white);font-size:12px;font-weight:600;border-radius:26px}
.heading{font-family:"Montserrat",sans-serif;font-weight:800;color:var(--ink);text-transform:uppercase}
.heading em{font-style:normal;color:var(--blue)}
.photo{position:absolute}

/* header / hero */
.hero{position:absolute;left:0;top:0;width:1200px;height:690px;background:var(--cream)}
.brand{position:absolute;display:flex;align-items:center;gap:10px;font-family:"Poppins",sans-serif;font-weight:600;color:var(--blue)}
.brand .dot{border-radius:50%;background:var(--blue)}
.nav{position:absolute;left:300px;top:34px;display:flex;gap:30px;font-size:11px;color:var(--ink);align-items:center}
.nav .home{width:14px;height:14px}
.hero-title{position:absolute;left:88px;top:168px;font-family:"Montserrat",sans-serif;font-weight:900;color:var(--ink);font-size:40px;line-height:1}
.hero-title .big{display:block;font-family:"Anton",sans-serif;font-weight:400;color:var(--blue);font-size:104px;line-height:1.02;letter-spacing:1px}
.hero-sub{position:absolute;left:88px;top:376px;width:360px;font-size:13px;color:var(--ink);line-height:1.4}
.dots{position:absolute;left:296px;top:459px;display:flex;gap:8px}
.dots span{width:9px;height:9px;border-radius:50%;background:#d4d4d4}
.dots span.on{background:var(--blue)}

/* welcome */
.welcome-text{position:absolute;left:624px;top:758px;width:480px}
.welcome-text p{font-size:11.5px;line-height:1.72;color:var(--ink);margin-top:26px}

/* team */
.team-title{position:absolute;left:0;width:1200px;top:1312px;text-align:center;color:var(--white);font-family:"Montserrat",sans-serif;font-weight:800;font-size:32px}
.team-lead{position:absolute;left:0;width:1200px;top:1360px;text-align:center;color:var(--white);font-size:11.5px;line-height:1.6}
.member{position:absolute;width:380px;text-align:center;color:var(--white)}
.member h3{font-size:15px;font-weight:500;text-transform:uppercase}
.member p{font-size:11.5px;line-height:1.65;margin-top:6px}
.ring{position:absolute;border-radius:50%}

/* projects */
.section-lead{position:absolute;left:0;width:1200px;text-align:center;font-size:11.5px;line-height:1.65;color:var(--ink)}
.card{position:absolute;width:282px;height:392px;border:1px solid var(--line);border-radius:14px;background:var(--white);text-align:center;padding:8px}
.card .img{height:210px;border-radius:10px}
.card h3{font-size:13.5px;font-weight:500;color:var(--ink);margin-top:22px;line-height:1.4;text-transform:uppercase}
.card p{font-size:11.5px;line-height:1.65;margin-top:8px;padding:0 14px}
.card a{display:block;margin-top:10px;color:var(--green);font-size:11px;font-weight:500;text-decoration:none}
.arrow{position:absolute;width:40px;height:40px;border-radius:50%;display:flex;align-items:center;justify-content:center}

/* publications */
.pub{position:absolute;width:432px;height:78px;border-radius:40px;background:var(--white);display:flex;align-items:center;padding:0 30px;font-size:11.5px;line-height:1.6;color:var(--ink)}
.pub.active{background:var(--orange);color:var(--white)}

/* resources */
.res{position:absolute;left:88px;width:546px;height:96px;border:1px solid var(--line);border-radius:40px;padding:18px 32px}
.res h4{font-size:12px;font-weight:600;color:var(--ink);text-transform:uppercase}
.res p{font-size:11px;line-height:1.65;color:var(--ink);margin-top:6px}

/* vision */
.vision-text{position:absolute;left:280px;width:640px;text-align:center;font-size:11.5px;line-height:1.7;color:var(--ink)}
.value{position:absolute;top:4196px;width:245px;height:234px;text-align:center;padding:48px 12px 0;font-size:11.5px;line-height:1.45}
.value h4{font-size:15px;font-weight:500;text-transform:uppercase;margin-bottom:12px;line-height:1.25}
.value.mid{background:var(--blue);color:var(--white);padding-top:22px}

/* contact */
.form{position:absolute;left:135px;top:4570px;width:480px;height:384px;background:var(--white);border-radius:14px;padding:40px 20px 0 20px}
.form h4{color:var(--blue);font-weight:500;font-size:16px;margin-left:12px}
.field{position:absolute;border:1px solid #d9d9d9;border-radius:26px;font-size:10px;color:var(--ink);padding:14px 22px}
.reach{position:absolute;left:700px;top:4700px;color:var(--white)}
.reach small{font-size:10px;letter-spacing:3px}
.reach h2{font-family:"Montserrat",sans-serif;font-weight:800;font-size:33px;margin-top:4px}
.reach p{font-size:11px;line-height:1.6;margin-top:4px;width:330px}

/* footer */
.footer{position:absolute;left:0;top:5012px;width:1200px;height:345px;background:var(--blue);color:var(--white)}
.footer h5{position:absolute;font-size:14px;font-weight:600}
.flist{position:absolute;font-size:11px;line-height:2}
.flist li{list-style:none}
.flist li::before{content:"›  ";}
.social{position:absolute;left:212px;top:150px;display:flex;gap:9px}
.social span{width:22px;height:22px;border-radius:50%;background:var(--white)}
.contact-line{position:absolute;left:594px;display:flex;gap:12px;font-size:11px;line-height:1.55}
.contact-line svg{flex:none;margin-top:2px}
.subscribe{position:absolute;left:806px;top:144px;width:236px;height:36px;background:var(--white);border-radius:20px;font-size:9.5px;color:#999;padding:11px 24px}
.subscribe .go{position:absolute;right:0;top:0;width:56px;height:36px;border-radius:20px;background:var(--green);display:flex;align-items:center;justify-content:center}
.copy{position:absolute;left:0;width:1200px;top:310px;text-align:center;font-size:11px}
</style>
</head>
<body>

<!-- HERO -->
<section class="hero">
  <div class="brand" style="left:88px;top:26px;font-size:27px"><span class="dot" style="width:34px;height:34px"></span>K7LAVE-Nest</div>
  <nav class="nav">
    <svg class="home" viewBox="0 0 14 14"><path d="M1 7 7 1.5 13 7v6H9V9H5v4H1z" fill="#1b8fd8"/></svg>
    <span>About Us</span><span>Research Areas</span><span>Ongoing Projects &amp; Recruitment</span><span>Publications</span><span>Resources</span>
  </nav>
  <div class="btn" style="left:972px;top:22px;width:140px;height:46px;font-size:11px">Contact Us</div>

  <h1 class="hero-title">ADVANCING BPD<span class="big">RESEARCH</span>AND RECOVERY</h1>
  <p class="hero-sub">Advancing science, innovation, and hope for BPD recovery</p>
  <div class="btn" style="left:88px;top:437px;width:140px;height:50px">Discover More</div>
  <div class="dots"><span></span><span class="on"></span><span></span><span></span></div>

  <div class="photo" role="img" aria-label="Clinician examining a patient's skin with a handheld mirror" style="left:575px;top:70px;width:545px;height:600px;background:radial-gradient(circle at 60% 40%,#dfe6ea 0,#c8cfd6 40%,rgba(251,240,228,0) 72%)"></div>
</section>
<svg class="abs" style="left:0;top:590px" width="1200" height="110" viewBox="0 0 1200 110">
  <path d="M0 70 Q600 -10 1200 40 L1200 110 L0 110 Z" fill="#fff"/>
  <path d="M0 72 Q250 22 520 30 Q300 32 0 80 Z" fill="#f0780f"/>
  <path d="M850 100 Q1020 98 1165 78 Q1010 110 850 100 Z" fill="#14a4a0"/>
</svg>

<!-- WELCOME -->
<svg class="abs" style="left:110px;top:720px" width="450" height="440" viewBox="0 0 450 440">
  <path d="M28 220 A200 200 0 0 0 322 400" stroke="#f0780f" stroke-width="8" fill="none" stroke-linecap="round"/>
</svg>
<div class="photo" role="img" aria-label="Researcher in a laboratory viewing microscope images on screens" style="left:128px;top:725px;width:420px;height:420px;border-radius:50%;background:linear-gradient(135deg,#e9eef3,#7fa6c8 55%,#1d5d94)"></div>
<div class="welcome-text">
  <h2 class="heading" style="font-size:33px;line-height:1.15"><em>WELCOME TO</em><br>OUR RESEARCH LAB</h2>
  <p>Welcome to the official website of our research lab, affiliated with TOBLAVE. We are committed to advancing scientific knowledge and developing innovative solutions to improve the lives of individuals living with Borderline Personality Disorder (BPD). Our work takes a comprehensive, multi-dimensional approach to recovery, integrating lifestyle medicine, psychosocial interventions, psychotherapeutic strategies, and biological treatments. Explore our ongoing research, meet our team, and discover the resources we offer to students, professionals, and individuals affected by BPD.</p>
</div>
<div class="btn" style="left:624px;top:1052px;width:142px;height:48px">Explore More</div>

<!-- TEAM -->
<svg class="abs" style="left:0;top:1248px" width="1200" height="690" viewBox="0 0 1200 690">
  <path d="M0 0 H1200 V640 Q800 575 600 620 Q300 660 0 665 Z" fill="#1b8fd8"/>
  <path d="M155 643 Q400 612 600 612 Q380 622 155 650 Z" fill="#f0780f"/>
  <path d="M640 612 Q900 600 1060 622 Q880 612 640 618 Z" fill="#f0780f"/>
</svg>
<h2 class="team-title">MEET K7LAVE-NEST TEAM</h2>
<p class="team-lead">Our researchers, students and partners work side by side<br>to advance understanding of Borderline Personality Disorder.</p>

<div class="ring" style="left:258px;top:1426px;width:250px;height:250px;border:4px solid transparent;border-left-color:#f0780f"></div>
<div class="photo" role="img" aria-label="Team member seated in an office" style="left:268px;top:1432px;width:236px;height:236px;border-radius:50%;background:linear-gradient(160deg,#cfd8e0,#6c8aa8)"></div>
<div class="member" style="left:185px;top:1700px"><h3>Team Members</h3><p>Our team is composed of passionate researchers, students, and healthcare professionals dedicated to advancing knowledge in the field of Borderline Personality Disorder (BPD).</p></div>

<div class="ring" style="left:712px;top:1426px;width:250px;height:250px;border:4px solid transparent;border-left-color:#f0780f"></div>
<div class="photo" role="img" aria-label="Researchers meeting at a table" style="left:722px;top:1432px;width:236px;height:236px;border-radius:50%;background:linear-gradient(160deg,#e2e6ea,#7d8f9f)"></div>
<div class="member" style="left:650px;top:1700px"><h3>Meet Our Researchers</h3><p>Our team is a dynamic group of faculty, researchers, and students working together to push the boundaries of BPD treatment and recovery.</p></div>

<div class="btn" style="left:508px;top:1833px;width:184px;height:44px;font-size:11px">Learn More About Us</div>

<!-- PROJECTS -->
<h2 class="heading abs" style="left:0;width:1200px;top:1988px;text-align:center;font-size:32px">ONGOING <em>PROJECTS</em></h2>
<p class="section-lead" style="top:2042px">Our research is driven by a commitment to advancing the understanding and treatment of Borderline Personality<br>Disorder. These projects are designed to improve the quality of life for individuals living with BPD.</p>

<div class="arrow" style="left:66px;top:2238px;background:var(--blue)"><svg width="10" height="10" viewBox="0 0 10 10"><path d="M6.5 2 3.5 5l3 3" stroke="#fff" stroke-width="1.5" fill="none"/></svg></div>
<div class="arrow" style="left:1093px;top:2238px;background:var(--teal)"><svg width="10" height="10" viewBox="0 0 10 10"><path d="M3.5 2l3 3-3 3" stroke="#fff" stroke-width="1.5" fill="none"/></svg></div>

<article class="card" style="left:159px;top:2118px">
  <div class="img" role="img" aria-label="Family preparing healthy food together" style="background:linear-gradient(150deg,#d9c6b2,#8b6f5a)"></div>
  <h3>Lifestyle<br>Medicine and BPD</h3>
  <p>This area focuses on understanding how lifestyle habits—such as sleep, physical activity…</p>
  <a>Read More</a>
</article>
<article class="card" style="left:459px;top:2118px">
  <div class="img" role="img" aria-label="Therapist talking with a patient" style="background:linear-gradient(150deg,#e6e1d8,#8f8a80)"></div>
  <h3>Interventions Supporting<br>Psychosocial Functioning</h3>
  <p>This area focuses on understanding how lifestyle habits—such as sleep, physical activity…</p>
  <a>Read More</a>
</article>
<article class="card" style="left:759px;top:2118px">
  <div class="img" role="img" aria-label="Clinician in gloves holding a test tube" style="background:linear-gradient(150deg,#f0f2f4,#9fb4c6)"></div>
  <h3>Biological<br>Treatments for BPD</h3>
  <p>Our lab is exploring the latest advances in biological treatments for BPD, focusing…</p>
  <a>Read More</a>
</article>
<div class="btn" style="left:508px;top:2546px;width:184px;height:48px;font-size:11px">Join Our Research Team</div>

<!-- PUBLICATIONS -->
<svg class="abs" style="left:0;top:2680px" width="1200" height="560" viewBox="0 0 1200 560">
  <path d="M0 85 Q300 30 600 10 Q900 -5 1200 45 V470 Q900 410 600 440 Q300 470 0 485 Z" fill="#1b8fd8"/>
  <path d="M30 105 Q220 40 400 25 Q210 50 30 112 Z" fill="#f0780f"/>
  <path d="M740 545 Q950 530 1170 495 Q960 545 740 552 Z" fill="#f0780f"/>
</svg>
<h2 class="abs" style="left:0;width:1200px;top:2745px;text-align:center;color:#fff;font-family:'Montserrat',sans-serif;font-weight:800;font-size:32px">PUBLICATIONS</h2>
<p class="section-lead" style="top:2794px;color:#fff">We are proud to share our latest research findings through peer-reviewed<br>publications and scientific contributions.</p>
<div class="pub" style="left:165px;top:2864px">Lifestyle Interventions in Borderline Personality<br>Disorder: A Review of Current Evidence</div>
<div class="pub" style="left:605px;top:2864px">The Role of Neuromodulation in the Treatment of Borderline<br>Personality Disorder: A Systematic Review</div>
<div class="pub active" style="left:165px;top:2952px">Psychosocial Integration and Social Functioning in<br>Borderline Personality Disorder: New Approaches</div>
<div class="pub" style="left:605px;top:2952px">Pharmacotherapy in Borderline Personality Disorder: Current<br>Trends and Future Directions</div>
<div class="pub" style="left:165px;top:3040px">Advances in Psychotherapy for Borderline Personality<br>Disorder: Personalized Approaches to Treatment</div>
<div class="pub" style="left:605px;top:3040px">Integrating Lifestyle Medicine into Borderline Personality<br>Disorder Treatment: A Holistic Approach</div>
<div class="btn" style="left:524px;top:3196px;width:152px;height:46px">View all</div>

<!-- STUDENT RESOURCES -->
<h2 class="heading abs" style="left:88px;top:3356px;font-size:33px">STUDENT <em>RESOURCES</em></h2>
<p class="abs" style="left:88px;top:3405px;width:540px;font-size:11.5px;line-height:1.65;color:var(--ink)">We are dedicated to supporting the educational and professional development of students in the field of mental health research.</p>
<div class="res" style="top:3468px"><h4>Research Tools</h4><p>Access to essential databases, academic journals, and research software tools.</p></div>
<div class="res" style="top:3572px"><h4>Training Opportunities</h4><p>Regular workshops, seminars, and conferences that focus on Borderline Personality Disorder and related research fields.</p></div>
<div class="res" style="top:3676px"><h4>Career Development</h4><p>Resources for career planning and professional growth within psychology, psychiatry, neuroscience, and other related disciplines.</p></div>
<div class="res" style="top:3780px"><h4>Mentorship Programs</h4><p>Direct access to faculty for guidance on research, academic development, and professional advice.</p></div>
<div class="photo" role="img" aria-label="Student reading a book in a library" style="left:663px;top:3334px;width:448px;height:586px;border-radius:224px 224px 0 0;background:linear-gradient(160deg,#b7a58c,#5c4a3c 60%,#2c2420)"></div>

<!-- VISION -->
<h2 class="heading abs" style="left:0;width:1200px;top:3974px;text-align:center;font-size:32px">VISION</h2>
<p class="vision-text" style="top:4028px">Affiliated with TOBLAVE, our laboratory is dedicated to creating tomorrow's interventions to offer a hopeful future for individuals living with Borderline Personality Disorder.</p>
<p class="vision-text" style="top:4088px;left:280px">Our vision is to design and develop innovative, person-centered solutions that support the full recovery of individuals with BPD. We aim to integrate and value each individual's needs, as well as their families and communities, in a holistic approach to treatment. By focusing on personal, social, functional, and physical recovery, we believe that a better future is possible.</p>
<div class="value" style="left:225px;color:var(--ink)"><h4>Hope</h4>We believe in the power of hope. Our research is driven by the belief that individuals living with BPD can lead fulfilling, meaningful lives. We strive to develop interventions that inspire optimism and offer a path</div>
<div class="value mid" style="left:480px"><h4>Empathy &amp;<br>Personalization</h4>We believe in the power of hope. Our research is driven by the belief that individuals living with BPD can lead fulfilling, meaningful lives. We strive to develop interventions that inspire optimism and offer a path</div>
<div class="value" style="left:735px;color:var(--ink)"><h4>Innovation</h4>At the heart of our research is a commitment to innovation. We continuously push the boundaries of knowledge, exploring new therapeutic methods and solutions to meet the evolving needs of individuals living with Borderline Personality Disorder.</div>

<!-- CONTACT -->
<svg class="abs" style="left:0;top:4500px" width="1200" height="520" viewBox="0 0 1200 520">
  <path d="M0 60 Q300 20 600 45 Q900 70 1200 35 V520 H0 Z" fill="#14a4a0"/>
  <path d="M720 42 Q950 80 1160 35 Q960 95 720 42 Z" fill="#f0780f"/>
</svg>
<div class="form">
  <h4>CONTACT US</h4>
  <div class="field" style="left:20px;top:70px;width:218px;height:42px">First Name*</div>
  <div class="field" style="left:244px;top:70px;width:218px;height:42px">Last Name*</div>
  <div class="field" style="left:20px;top:124px;width:218px;height:42px">Email Address*</div>
  <div class="field" style="left:244px;top:124px;width:218px;height:42px">Phone*</div>
  <div class="field" style="left:20px;top:178px;width:442px;height:88px;border-radius:18px">How we can help?</div>
  <div class="btn" style="left:20px;top:292px;width:152px;height:46px">Submit Request</div>
</div>
<div class="reach">
  <small>INTRODUCTION</small>
  <h2>REACH OUT TO US</h2>
  <p>Ready to take the next step? Contact Nordvale Group to learn how we can support your expansion and financing needs.</p>
</div>

<!-- FOOTER -->
<footer class="footer">
  <div class="brand" style="left:166px;top:92px;font-size:36px;color:#fff"><span class="dot" style="width:40px;height:40px;background:#fff"></span>K7LAVE-Nest</div>
  <div class="social"><span></span><span></span><span></span><span></span></div>

  <h5 style="left:427px;top:54px">Information</h5>
  <ul class="flist" style="left:430px;top:86px">
    <li>About Us</li><li>Research Areas</li><li>Ongoing Projects</li><li>&amp; Recruitment</li><li>Publications</li><li>Resources</li><li>Contact Us</li>
  </ul>

  <h5 style="left:590px;top:54px">Contact Us</h5>
  <div class="contact-line" style="top:100px"><svg width="12" height="12" viewBox="0 0 12 12"><path d="M2.5 1 4.5 1 5.5 3.5 4 4.5Q5 7 7.5 8L8.5 6.5 11 7.5V9.5Q11 11 9.5 11 1 10 1 2.5 1 1 2.5 1Z" fill="#fff"/></svg>+41 70 123 45 67</div>
  <div class="contact-line" style="top:140px"><svg width="12" height="12" viewBox="0 0 12 12"><rect x="1" y="2.5" width="10" height="7" fill="#fff"/><path d="M1 2.5 6 6.5 11 2.5" stroke="#1b8fd8" fill="none"/></svg><span style="text-decoration:underline">hello@nordvalegroup.ch</span></div>
  <div class="contact-line" style="top:178px"><svg width="12" height="12" viewBox="0 0 12 12"><path d="M6 11.5Q2 7 2 4.5a4 4 0 0 1 8 0Q10 7 6 11.5Z" fill="#fff"/><circle cx="6" cy="4.5" r="1.4" fill="#1b8fd8"/></svg><span>Nordvale Group AG<br>Lindenweg 12<br>CH-6300 Zug</span></div>

  <h5 style="left:808px;top:54px">Subscribe Newsletter</h5>
  <p class="abs" style="left:810px;top:96px;font-size:10px;line-height:1.6">Subscribe newsletter for the latest<br>offers and news</p>
  <div class="subscribe">Enter Email...<span class="go"><svg width="16" height="10" viewBox="0 0 16 10"><path d="M1 5h13M10 1l4 4-4 4" stroke="#fff" stroke-width="1.6" fill="none"/></svg></span></div>

  <p class="copy">2025 Copyright © Fieldnote All Rights Reserved.</p>
</footer>

</body>
</html>
```